Local Roofing/Construction company business needs new biz card design

We need a new business card design, current cards are from the start of this operation and generic at best. We are a local Construction Company (General Contractor) with a majority of our work originating from insurance claims-exterior finish work is the main focus (Roofs-Siding-Gutters etc). Heavily involved with homeowners and the low ball offers they receive from insurance company's after a insurable event takes place. I have attached some of our original logo file(s) below.

```html
<!DOCTYPE html>
<html lang="en">
<head>
<meta charset="utf-8">
<title>Stonegate Construction – Business Card</title>
<link href="https://fonts.googleapis.com/css2?family=Montserrat:wght@400;500;700&display=swap" rel="stylesheet">
<style>
  :root {
    --backdrop: #141414;
    --card: #212121;
    --card-deep: #1a1a1a;
    --emboss: #111111;
    --green: #2fd67a;
    --ink-light: #f2f2ee;
    --ink-muted: #d9d9d9;
  }
  * { box-sizing: border-box; margin: 0; padding: 0; }
  html, body {
    width: 1200px; height: 900px; overflow: hidden;
    background: var(--backdrop);
    font-family: "Montserrat", sans-serif;
  }
  .sheet {
    width: 1200px; height: 900px;
    display: flex; flex-direction: column;
    align-items: center; justify-content: center; gap: 40px;
  }
  .card {
    position: relative;
    width: 620px; height: 354px;
    background: var(--card);
    border-radius: 22px;
    border-bottom: 5px solid var(--green);
    overflow: hidden;
  }

  /* Front */
  .card-front {
    display: flex; align-items: center; justify-content: center;
  }
  .front-wordmark {
    display: flex; align-items: center; gap: 22px;
    color: var(--emboss);
    font-weight: 700;
    text-transform: uppercase;
  }
  .front-wordmark .mark-square {
    width: 64px; height: 64px; background: var(--emboss); border-radius: 6px;
  }
  .front-wordmark .name {
    font-size: 42px; line-height: 1; letter-spacing: 1px;
  }
  .front-wordmark .name span {
    display: block; font-size: 22px; letter-spacing: 4px; margin-top: 6px;
  }

  /* Back */
  .card-back {
    display: grid;
    grid-template-columns: 290px 1px 1fr;
    align-items: center;
    padding: 0 36px 0 40px;
  }
  .brand-block {
    display: flex; flex-direction: column; align-items: center; gap: 14px;
  }
  .brand-block .mark-square {
    width: 160px; height: 160px; background: var(--green); border-radius: 18px;
  }
  .brand-block .brand-name {
    color: var(--green); font-weight: 700; font-size: 17px;
    letter-spacing: 2px; text-transform: uppercase; text-align: center;
  }
  .divider {
    width: 1px; height: 170px; background: var(--green);
  }
  .contact {
    padding-left: 34px; color: var(--ink-light);
  }
  .contact .person {
    color: var(--green); font-weight: 700; font-size: 28px; line-height: 1.1;
  }
  .contact .role {
    font-size: 15px; color: var(--ink-muted); margin-bottom: 18px;
  }
  .contact ul { list-style: none; }
  .contact li {
    display: flex; align-items: flex-start; gap: 10px;
    font-size: 14px; line-height: 1.45; margin-bottom: 4px;
  }
  .contact li svg {
    flex: 0 0 14px; width: 14px; height: 14px; margin-top: 3px; fill: var(--green);
  }
</style>
</head>
<body>
<main class="sheet">
  <section class="card card-front" aria-label="Card front">
    <div class="front-wordmark">
      <div class="mark-square"></div>
      <div class="name">Stonegate<span>Construction</span></div>
    </div>
  </section>

  <section class="card card-back" aria-label="Card back">
    <div class="brand-block">
      <div class="mark-square"></div>
      <div class="brand-name">Stonegate Construction</div>
    </div>
    <div class="divider"></div>
    <div class="contact">
      <p class="person">Daniel Harper</p>
      <p class="role">Owner</p>
      <ul>
        <li>
          <svg viewBox="0 0 24 24" aria-hidden="true"><path d="M6.6 10.8a15.1 15.1 0 0 0 6.6 6.6l2.2-2.2a1 1 0 0 1 1-.25 11.4 11.4 0 0 0 3.6.57 1 1 0 0 1 1 1V20a1 1 0 0 1-1 1A17 17 0 0 1 3 4a1 1 0 0 1 1-1h3.5a1 1 0 0 1 1 1c0 1.25.2 2.45.57 3.57a1 1 0 0 1-.25 1z"/></svg>
          <span>555-014-2290</span>
        </li>
        <li>
          <svg viewBox="0 0 24 24" aria-hidden="true"><path d="M2 5h20v14H2zm2 2v.4l8 5 8-5V7zm0 2.8V17h16V9.8l-8 5z"/></svg>
          <span>info@stonegatebuilds.com<br>www.stonegatebuilds.com</span>
        </li>
        <li>
          <svg viewBox="0 0 24 24" aria-hidden="true"><path d="M12 2a7 7 0 0 0-7 7c0 5.2 7 13 7 13s7-7.8 7-13a7 7 0 0 0-7-7zm0 9.5A2.5 2.5 0 1 1 12 6.5a2.5 2.5 0 0 1 0 5z"/></svg>
          <span>48 Alder Ridge Rd<br>Fairview, MO 63000</span>
        </li>
      </ul>
    </div>
  </section>
</main>
</body>
</html>
```